Cat-products company needs smart, yet endearing, business card

We need a business card design for a new, but up-and-running, business based in Honolulu, Hawaii. The business is Purrlane Nest Co. Our first product is the most environmentally-friendly cat grass kit ever seen on the planet. Future products, currently in the R&D phase, will include a variety of exciting cat scratchers. We also do consulting work to help apartment-dwellers make their home more cat-friendly and, in the future, plan on doing full, custom installs of structure to create high walkways for cats.

Target Market(s)

Middle-aged, apartment-dwelling, middle-class workers who own 1 or more cats and who dote on them.

Industry/Entity Type

Pet Care

Contact Information for Business Card

A striking, professional, yet warm and friendly design is what we're after.

Font styles to use
Serif
Sans Serif
Other font styles liked:
• Comfortaa

Colors

Designer to choose colors to be used in the design.

Requirements
Must have
• The company logo: (see attachment)
• The company name: Purrlane Nest Co
• The web address: www.purrlanenestco.example
• Email: support@purrlanenestco.example
• Phone: +1 (808) 555 0172
• Update (Fri Jun 30 3017 7:45pm Hawaii Time) I would like, is possible, uploaded picture of the cat grass kit on the back of the card with some text along the lines of: Purrlane Nest Co - Where The Freshest Kitty Sprouts Begin
Nice to have
• A cat picture, cartoon, real or silhouette that illustrates cats in action and/or relaxing; ie using the apartment space to live, play and relax in and being well-contented.
• Most of the website is done in the font: Comfortaa. It might be nice to continue using this for brand consistency.
Should not have
• Hard-to-read fonts.

```html
<!DOCTYPE html>
<html lang="en">
<head>
<meta charset="UTF-8">
<title>Purrlane Nest Co – Business Card</title>
<link rel="stylesheet" href="https://fonts.googleapis.com/css2?family=Comfortaa:wght@400;700&display=swap">
<style>
  :root {
    --page-bg: #1c1c1c;
    --card-bg: #141414;
    --card-edge: #202020;
    --gold: #f5b40f;
    --brown: #5a3c2e;
    --icon-ring: #e08a12;
    --white: #ffffff;
    --muted-logo: #3a3a3a;
    --rule: #cfcfcf;
  }
  * { margin: 0; padding: 0; box-sizing: border-box; }
  html, body {
    width: 1200px; height: 1200px; overflow: hidden;
    background: var(--page-bg);
    font-family: 'Comfortaa', sans-serif;
  }
  .canvas { position: relative; width: 1200px; height: 1200px; }
  .card {
    position: absolute; left: 160px; width: 880px; height: 503px;
    background: var(--card-bg);
    border: 1px solid var(--card-edge);
    box-shadow: 0 10px 30px rgba(0,0,0,0.5);
  }
  .card--back { top: 70px; }
  .card--front { top: 627px; }

  .back-wordmark {
    position: absolute; inset: 0;
    display: flex; align-items: center; justify-content: center;
    font-weight: 700; font-size: 64px; color: var(--muted-logo);
  }

  .front-brand {
    position: absolute; left: 50px; top: 0; bottom: 0; width: 330px;
    display: flex; align-items: center; gap: 16px;
  }
  .brand-dot { width: 46px; height: 46px; border-radius: 50%; background: var(--brown); flex: none; }
  .brand-name { font-weight: 700; font-size: 40px; line-height: 1.15; color: var(--gold); }

  .divider {
    position: absolute; left: 420px; top: 130px; width: 2px; height: 230px;
    background: var(--rule);
  }

  .contact { position: absolute; left: 460px; top: 140px; color: var(--white); }
  .person-name { font-weight: 700; font-size: 34px; }
  .person-title { font-weight: 700; font-size: 22px; color: var(--gold); margin-top: 4px; }
  .contact-list { list-style: none; margin-top: 26px; }
  .contact-item { display: flex; align-items: center; gap: 16px; font-size: 22px; height: 48px; }
  .contact-icon { width: 40px; height: 40px; flex: none; }
</style>
</head>
<body>
<main class="canvas">
  <section class="card card--back" aria-label="Card back">
    <div class="back-wordmark">Purrlane Nest Co</div>
  </section>

  <section class="card card--front" aria-label="Card front">
    <div class="front-brand">
      <span class="brand-dot"></span>
      <span class="brand-name">Purrlane<br>Nest Co</span>
    </div>
    <div class="divider"></div>
    <div class="contact">
      <p class="person-name">Kalena Morishita</p>
      <p class="person-title">President</p>
      <ul class="contact-list">
        <li class="contact-item">
          <svg class="contact-icon" viewBox="0 0 40 40" aria-hidden="true">
            <circle cx="20" cy="20" r="18" fill="#3a2414" stroke="var(--icon-ring)" stroke-width="3"/>
            <path d="M12 17c0-3 16-3 16 0v2h-4v-2h-8v2h-4z M14 21h12l2 7H12z" fill="var(--icon-ring)"/>
          </svg>
          +1 (808) 555 0172
        </li>
        <li class="contact-item">
          <svg class="contact-icon" viewBox="0 0 40 40" aria-hidden="true">
            <circle cx="20" cy="20" r="18" fill="#3a2414" stroke="var(--icon-ring)" stroke-width="3"/>
            <rect x="11" y="14" width="18" height="12" fill="none" stroke="var(--icon-ring)" stroke-width="2"/>
            <path d="M11 14l9 7 9-7" fill="none" stroke="var(--icon-ring)" stroke-width="2"/>
          </svg>
          support@purrlanenestco.example
        </li>
        <li class="contact-item">
          <svg class="contact-icon" viewBox="0 0 40 40" aria-hidden="true">
            <circle cx="20" cy="20" r="18" fill="#3a2414" stroke="var(--icon-ring)" stroke-width="3"/>
            <g fill="none" stroke="var(--icon-ring)" stroke-width="1.8">
              <circle cx="20" cy="20" r="9"/>
              <ellipse cx="20" cy="20" rx="4" ry="9"/>
              <path d="M11 20h18M13 15h14M13 25h14"/>
            </g>
          </svg>
          www.purrlanenestco.example
        </li>
      </ul>
    </div>
  </section>
</main>
</body>
</html>
```